The Quillmore Daily Ledger

I am making a journal for tracking pain symptoms for TMJ (Jaw) pain. I have the cover designed and I just need the journal page designed that will repeat throughout the journal. The journal is the image on the left of the bundle. The page I would like to be developed is the picture that I hand sketched out. It should be a 6 x 9 page, similar to the attached example. Greyscale, no color. Thank you!

Target Market(s)

20-55 year old women

Industry/Entity Type

Healthcare

Colors

Designer to choose only greyscale colors for use in the design.

Requirements
Must have
• A neat, well-designed page with the content I have sketched out by hand.
Nice to have
• Creative display of the content I provided and development of the pain scale and pain diagram faces in a professional looking way.

```html
<!DOCTYPE html>
<html lang="en">
<head>
<meta charset="utf-8">
<title>The Quillmore Daily Ledger – Daily Page</title>
<link rel="stylesheet" href="https://fonts.googleapis.com/css2?family=Montserrat:wght@400;500;600;700&display=swap">
<style>
:root{
  --bg:#a9a9a9;
  --paper:#ffffff;
  --bar:#3d3d3d;
  --head:#dcdcdc;
  --soft:#f3f3f3;
  --brand:#3d3d3d;
  --ink:#2b2b2b;
  --rule:#c9c9c9;
  --check:#8a8a8a;
  --face:#e4e4e4;
  --face-line:#555555;
  --art:#d6d6d6;
  --divider:#ffffff;
}
*{box-sizing:border-box;margin:0;padding:0}
html,body{width:800px;height:1200px;overflow:hidden;background:var(--bg)}
body{font-family:"Montserrat",Arial,sans-serif;color:var(--ink);font-size:16px}
.page{position:absolute;left:21px;top:30px;width:758px;height:1140px;background:var(--paper)}
.page > *{position:absolute}
.brand{left:0;width:758px;top:48px;display:flex;justify-content:center;align-items:center;gap:10px}
.brand-dot{width:34px;height:34px;border-radius:50%;background:var(--bar)}
.brand-name{font-weight:600;font-size:18px;color:var(--brand)}
.meta{left:41px;width:680px;top:118px;display:flex;gap:30px;font-size:15px}
.meta-field{display:flex;align-items:flex-end;flex:1;gap:6px}
.meta-field .line{flex:1;border-bottom:1px solid var(--rule);height:12px}
.bar{left:41px;width:680px;height:25px;background:var(--bar);color:#fff;border-radius:5px 5px 0 0;
  font-weight:600;font-size:15px;text-align:center;line-height:25px}
.time-table{left:41px;top:182px;width:680px;border-collapse:collapse;font-size:15px}
.time-table th{background:var(--head);font-weight:500;height:25px;border-left:2px solid var(--divider)}
.time-table td{background:var(--soft);height:19px;font-size:12px;padding-left:30px;border-left:2px solid var(--divider)}
.scale-num{top:290px;font-size:20px;transform:translateX(-50%)}
.face{width:60px;height:60px;border-radius:50%;background:var(--face);border:2px solid var(--face-line);transform:translate(-50%,-50%);top:350px}
.scale-label{top:387px;font-size:16px;transform:translateX(-50%);white-space:nowrap}
.panel{left:41px;width:680px;background:var(--soft);border:1px solid #e3e3e3}
.art{background:var(--art);border-radius:6px}
.art-label{font-size:15px;top:526px;transform:translateX(-50%);white-space:nowrap}
.opt-col{top:444px;height:111px;border-left:2px solid var(--divider)}
.opt-col h3{background:var(--head);font-size:12px;font-weight:700;color:#3c3c3c;text-align:center;height:22px;line-height:22px;letter-spacing:.3px}
.opt-list{list-style:none;padding:10px 0 0 30px;font-size:16px;line-height:21px}
.box{display:inline-block;width:11px;height:11px;border:1px solid var(--check);margin-right:9px;vertical-align:0}
.check-grid{display:grid;grid-template-columns:210px 244px 226px;height:100%}
.check-grid ul{list-style:none;padding:11px 0 0 28px;font-size:16px;line-height:21.5px;border-left:2px solid var(--divider)}
.check-grid ul:first-child{border-left:none}
.fill{display:inline-block;width:104px;border-bottom:1px solid var(--rule);margin-left:6px}
.fill-wide{display:inline-block;width:156px;border-bottom:1px solid var(--rule)}
.state{left:41px;width:680px;font-size:16px;line-height:21px}
.state .box{margin-left:14px;margin-right:6px}
.notes{left:41px;top:1006px;width:680px;height:91px;border:1px solid var(--rule);border-top:none}
.notes div{height:23px;border-bottom:1px solid var(--rule)}
</style>
</head>
<body>
<main class="page">
  <header class="brand">
    <span class="brand-dot"></span>
    <span class="brand-name">The Quillmore Daily Ledger</span>
  </header>

  <div class="meta">
    <div class="meta-field">DATE:<span class="line"></span></div>
    <div class="meta-field">DAY OF THE WEEK:<span class="line"></span></div>
  </div>

  <div class="bar" style="top:154px">TIME</div>
  <table class="time-table">
    <colgroup><col style="width:66px"><col style="width:95px"><col style="width:90px"><col style="width:87px"><col style="width:66px"><col style="width:94px"><col style="width:91px"><col style="width:91px"></colgroup>
    <tr><th style="border-left:none"></th><th>begin</th><th>end</th><th>duraion</th><th></th><th>begin</th><th>end</th><th>duraion</th></tr>
    <tr><td style="border-left:none">1</td><td></td><td></td><td></td><td>3</td><td></td><td></td><td></td></tr>
    <tr><td style="border-left:none">2</td><td></td><td></td><td></td><td>4</td><td></td><td></td><td></td></tr>
  </table>

  <div class="bar" style="top:258px">SEVERITY OF PAIN (Circle Range)</div>
  <span class="scale-num" style="left:59px">1</span>
  <span class="scale-num" style="left:137px">2</span>
  <span class="scale-num" style="left:196px">3</span>
  <span class="scale-num" style="left:260px">4</span>
  <span class="scale-num" style="left:333px">5</span>
  <span class="scale-num" style="left:398px">6</span>
  <span class="scale-num" style="left:468px">7</span>
  <span class="scale-num" style="left:536px">8</span>
  <span class="scale-num" style="left:605px">9</span>
  <span class="scale-num" style="left:693px">10</span>
  <div class="face" style="left:105px" role="img" aria-label="Pain scale icon: no pain"></div>
  <div class="face" style="left:204px" role="img" aria-label="Pain scale icon: mild"></div>
  <div class="face" style="left:320px" role="img" aria-label="Pain scale icon: moderate"></div>
  <div class="face" style="left:431px" role="img" aria-label="Pain scale icon: severe"></div>
  <div class="face" style="left:546px" role="img" aria-label="Pain scale icon: very severe"></div>
  <div class="face" style="left:654px" role="img" aria-label="Pain scale icon: worst pain possible"></div>
  <span class="scale-label" style="left:204px">mild</span>
  <span class="scale-label" style="left:320px">moderate</span>
  <span class="scale-label" style="left:430px">severe</span>
  <span class="scale-label" style="left:598px">very severe worst pain posible</span>

  <div class="bar" style="top:419px">LOCATION</div>
  <div class="panel" style="top:444px;height:111px;background:#fff"></div>
  <div class="art" style="left:55px;top:455px;width:54px;height:64px" role="img" aria-label="Head illustration highlighting the jaw joint"></div>
  <div class="art" style="left:126px;top:455px;width:47px;height:64px" role="img" aria-label="Head illustration highlighting the jaw muscles"></div>
  <div class="art" style="left:186px;top:455px;width:46px;height:64px" role="img" aria-label="Head illustration highlighting the neck"></div>
  <div class="art" style="left:249px;top:455px;width:49px;height:64px" role="img" aria-label="Head illustration highlighting tension headache area"></div>
  <div class="art" style="left:312px;top:470px;width:60px;height:30px" role="img" aria-label="Illustration of teeth"></div>
  <span class="art-label" style="left:82px">jmt</span>
  <span class="art-label" style="left:148px">muscles</span>
  <span class="art-label" style="left:210px">neck</span>
  <span class="art-label" style="left:273px">tension</span>
  <span class="art-label" style="left:342px">teeth</span>
  <section class="opt-col" style="left:385px;width:169px">
    <h3>CLICK/POP</h3>
    <ul class="opt-list"><li><span class="box"></span>increased</li><li><span class="box"></span>decreased</li><li><span class="box"></span>no change</li></ul>
  </section>
  <section class="opt-col" style="left:554px;width:167px">
    <h3>OPENING ABILITY</h3>
    <ul class="opt-list"><li><span class="box"></span>increased</li><li><span class="box"></span>decreased</li><li><span class="box"></span>no change</li></ul>
  </section>

  <div class="bar" style="top:568px">TRIGGERS(Check all that apply)</div>
  <div class="panel" style="top:593px;height:111px">
    <div class="check-grid">
      <ul><li><span class="box"></span>Sleep</li><li><span class="box"></span>First thing in AM</li><li><span class="box"></span>Clenching</li><li><span class="box"></span>Insomnia</li></ul>
      <ul><li><span class="box"></span>Weather</li><li><span class="box"></span>Eating</li><li><span class="box"></span>Work</li><li><span class="box"></span>Opening wide/ yawn</li></ul>
      <ul><li><span class="box"></span>PMS/ menstration</li><li><span class="box"></span>Stress at home</li><li><span class="box"></span>Stress at work</li><li><span class="box"></span>Other<span class="fill"></span></li></ul>
    </div>
  </div>

  <p class="state" style="top:718px">My jaw was <span class="box"></span>relaxed <span class="box"></span>clenched <span class="box"></span>tense</p>
  <p class="state" style="top:746px">My breathing was <span class="box"></span>shallow/tense <span class="box"></span>deep/relaxed switch these <span class="box"></span>deep/relaxed<br><span class="box" style="margin-left:0"></span>shallow/tense</p>
  <p class="state" style="top:799px">My neck/shoulders were <span class="box"></span>relaxed <span class="box"></span>tense <span class="box"></span>shouched <span class="box"></span>upright</p>

  <div class="bar" style="top:836px">RELIEF MEASURES(Check all that apply)</div>
  <div class="panel" style="top:861px;height:109px">
    <div class="check-grid">
      <ul style="padding-left:14px"><li><span class="box"></span>Deep breathing</li><li><span class="box"></span>Teeth apart/relax/jaw</li><li><span class="box"></span>Self-massage</li><li><span class="box"></span>Heart/coldcircle)</li></ul>
      <ul><li><span class="box"></span>Medication</li><li><span class="box"></span>Rest</li><li><span class="box"></span>Gentle stretching</li><li><span class="box"></span>Posture correction</li></ul>
      <ul style="padding-left:20px"><li><span class="box"></span>Mindful reset</li><li><span class="box"></span>Stabilization exercise</li><li><span class="box"></span>Other<span class="fill"></span></li><li><span class="box"></span><span class="fill-wide"></span></li></ul>
    </div>
  </div>

  <div class="bar" style="top:981px">NOTES AND PLAN TO AVOID TRIGGERS</div>
  <div class="notes"><div></div><div></div><div></div><div style="border-bottom:none"></div></div>
</main>
</body>
</html>
```